Income Tax and Accounting Brochure

I need a brochure using my new logo (file attached). I do tax work and accounting work. I am an EA (QDX Enrolled Agent - logo attached) and would like this incorporated into the brochure. I also have a MSA in Accounting. Please incorporate the text that I have provided in the brochure.

Target Market(s)

Tax Clients - both business and individuals

Industry/Entity Type

Accounting

Colors
0054AA
0677BA
7BADD7
CADEEF
E8F1F8

Requirements
Must have
• Use my logo and the QDX EA file in the brochure
Nice to have
• I would like to see a brochure that I can customize with my own text if possible.

```html
<!DOCTYPE html>
<html lang="en">
<head>
<meta charset="utf-8">
<title>Ridgeline Accounting Brochure</title>
<link rel="stylesheet" href="https://fonts.googleapis.com/css2?family=Montserrat:wght@400;500;600;700;800&family=Barlow+Semi+Condensed:wght@500;700&display=swap">
<style>
:root{
  --bg:#d6d6d6;
  --paper:#ffffff;
  --navy:#1a4c9c;
  --blue:#0054aa;
  --blue-mid:#0677ba;
  --blue-soft:#7badd7;
  --blue-pale:#cadeef;
  --blue-ice:#e8f1f8;
  --red:#c41f3b;
  --crimson:#b22a4e;
  --ink:#1d1d2b;
  --white:#ffffff;
}
*{margin:0;padding:0;box-sizing:border-box}
html,body{width:1200px;height:678px;overflow:hidden;background:var(--bg);font-family:"Montserrat",sans-serif;color:var(--ink)}
.canvas{position:relative;width:1200px;height:678px}
.spread{position:absolute;top:157px;height:376px;background:var(--paper);overflow:hidden;box-shadow:0 8px 22px rgba(0,0,0,.18)}
.spread--inside{left:72px;width:520px}
.spread--outside{left:649px;width:491px}
.panel{position:absolute;top:0;height:100%}
.abs{position:absolute}

/* inside spread */
.media-illustration{left:207px;top:38px;width:108px;height:100px;border-radius:40% 50% 45% 50%;background:radial-gradient(circle at 50% 55%,#b9c6ee 0%,#d9e0f6 60%,rgba(255,255,255,0) 75%)}
.media-hand{left:110px;top:130px;width:300px;height:246px;background:linear-gradient(110deg,rgba(255,255,255,0) 0%,rgba(226,232,240,.7) 35%,rgba(214,186,166,.55) 70%,rgba(240,240,244,.4) 100%)}
.title{left:24px;top:116px;font-weight:800;font-size:13.5px;line-height:15px}
.title{top:30px}
.title .t-red{color:var(--red);display:block}
.title .t-blue{color:var(--blue);display:block}
.body-copy{left:24px;width:140px;font-size:6.9px;line-height:8.9px;font-weight:500}
.body-copy p+p{margin-top:5px}
.rule{left:24px;top:248px;width:133px;height:5px;background:var(--blue)}
.pull-quote{left:24px;top:268px;width:170px;font-size:11.6px;line-height:15.4px;color:var(--blue);font-weight:500}
.web{font-size:6.4px;color:var(--blue);font-weight:500}
.web--inside{left:24px;top:347px}
.red-line{left:118px;top:350px;width:400px;height:1px;background:var(--red)}
.panel--benefits{left:352px;width:168px;background:var(--navy)}
.tag{left:14px;top:22px;padding:3px 6px;background:var(--red);color:var(--white);font-weight:700;font-size:8.4px;letter-spacing:.1px}
.benefits{left:14px;top:48px;width:146px;list-style:none}
.benefits li{position:relative;padding-left:17px;font-size:6.2px;line-height:8.8px;color:var(--white);margin-bottom:6px}
.benefits li svg{position:absolute;left:0;top:1px}
.books-box{left:14px;top:238px;width:133px;height:118px;background:rgba(123,173,215,.35);padding:10px 9px 0 9px;border-left:0}
.books-box .bar{position:absolute;left:0;top:10px;width:4px;height:18px;background:var(--red)}
.books-box h3{font-size:8.4px;line-height:11px;color:var(--white);font-weight:700}
.books-box p{margin-top:8px;font-size:5.9px;line-height:7.7px;color:var(--white)}

/* outside spread */
.crimson{background:var(--crimson)}
.band-blue{background:linear-gradient(90deg,var(--blue) 0%,#1c5db0 100%)}
.about{left:19px;top:110px;width:125px;color:var(--white)}
.about h2{font-size:9px;line-height:11px;font-weight:700}
.about p{margin-top:8px;font-size:6.1px;line-height:8.3px}
.media-tech{left:176px;top:0;width:315px;height:293px;background:linear-gradient(120deg,#2c7bb2 0%,#1d9fb9 35%,#1a3f83 65%,#0c2a63 100%)}
.firm-box{left:188px;top:95px;width:97px;height:142px;background:rgba(40,90,150,.55);padding:10px 9px;color:var(--white);font-size:8px;line-height:9.8px}
.contact{left:176px;color:var(--white);font-size:6.2px;line-height:8.2px}
.headline{left:360px;top:197px;color:var(--white);font-family:"Barlow Semi Condensed",sans-serif;line-height:1}
.headline .h-small{display:block;font-size:19px;font-weight:500;line-height:19px}
.headline .h-big{display:block;font-size:26px;font-weight:700;line-height:25px;margin-top:4px}
.brand{left:362px;top:316px;display:flex;align-items:center;gap:6px}
.brand .dot{width:14px;height:14px;border-radius:50%;background:var(--blue)}
.brand span{font-size:7.2px;font-weight:700;color:var(--blue);line-height:9px}
</style>
</head>
<body>
<main class="canvas">

  <section class="spread spread--inside" aria-label="Brochure inside spread">
    <div class="abs media-hand" role="img" aria-label="Photo of a hand touching a digital interface with finance icons"></div>
    <div class="abs media-illustration" role="img" aria-label="Illustration of people reviewing charts and reports"></div>

    <h1 class="abs title"><span class="t-red">Tax Preparation</span><span class="t-blue">why hire us?</span></h1>
    <div class="abs body-copy" style="top:72px">
      <p>Preparing your own income tax return can be a task that leaves you with more questions than answers. According to a study released by the US Government’s Federal Review Office last year, most taxpayers (77% of 71 million taxpayers) believe they benefited from using a professional tax preparer.</p>
      <p>Whether we like it or not, today’s tax laws are so complicated that filing a relatively simple return can be confusing. It is just too easy to overlook deductions and credits to which you are entitled. Even if you use a computer software program there’s no substitute for the assistance of an experienced tax professional.</p>
    </div>
    <div class="abs rule"></div>
    <p class="abs pull-quote">With Ridgeline Accounting &amp; Consulting, LLC, each client receives close personal and professional attention.</p>
    <p class="abs web web--inside">www.ridgelineacct.com</p>
    <div class="abs red-line"></div>

    <div class="panel panel--benefits">
      <div class="abs tag">HERE’S WHAT YOUR GET...</div>
      <ul class="abs benefits">
        <li><svg width="7" height="7" viewBox="0 0 8 8"><circle cx="4" cy="4" r="4" fill="#fff"/><path d="M3 2.2 4.8 4 3 5.8" stroke="#c41f3b" stroke-width="1.1" fill="none"/></svg>Your tax return will be checked and rechecked by our computer software identifying potential problems the QDX may look at more closely and reviewing the math to limit QDX contacts.</li>
        <li><svg width="7" height="7" viewBox="0 0 8 8"><circle cx="4" cy="4" r="4" fill="#fff"/><path d="M3 2.2 4.8 4 3 5.8" stroke="#c41f3b" stroke-width="1.1" fill="none"/></svg>Your tax return can be filed electronically so you will get a refund back quicker.</li>
        <li><svg width="7" height="7" viewBox="0 0 8 8"><circle cx="4" cy="4" r="4" fill="#fff"/><path d="M3 2.2 4.8 4 3 5.8" stroke="#c41f3b" stroke-width="1.1" fill="none"/></svg>Our staff will show you how to adjust your payroll withholding to get more money back each week. Why give the QDX an interest free loan for up to 16 months.</li>
        <li><svg width="7" height="7" viewBox="0 0 8 8"><circle cx="4" cy="4" r="4" fill="#fff"/><path d="M3 2.2 4.8 4 3 5.8" stroke="#c41f3b" stroke-width="1.1" fill="none"/></svg>We will show you potential deductions to limit your tax liability for next year. In addition, we will give you a sheet of commonly overlooked deductions to limit the following year’s tax liability.</li>
      </ul>
      <div class="abs books-box">
        <div class="bar"></div>
        <h3>BOOKS A MESS:<br>NO PROBLEM!</h3>
        <p>If you own a small business and haven’t kept up your bookkeeping, don’t worry. We can help you. We’ll prepare your bookkeeping for the year, prepare a full Schedule C, as well as your personal income tax return. Then we’ll help you set up an easy system that allows you to keep your books in tip-top shape next year.</p>
      </div>
    </div>
  </section>

  <section class="spread spread--outside" aria-label="Brochure outside spread">
    <div class="abs crimson" style="left:0;top:0;width:491px;height:296px"></div>
    <div class="abs band-blue" style="left:0;top:296px;width:333px;height:57px"></div>
    <div class="abs" style="left:0;top:353px;width:491px;height:23px;background:var(--blue-ice)"></div>
    <div class="abs" style="left:333px;top:293px;width:158px;height:83px;background:var(--white)"></div>

    <div class="abs about">
      <h2>About Marion T Haskell,<br>MSA EA (Principal)</h2>
      <p>I have a Masters’ Degree in accounting and am an QDX Enrolled Agent. I am also a LedgerBooks Advanced Certified Consultant in both the online and desktop products including Enterprise and Point of Sale. I provide individual and small business tax services, Accounting, bookkeeping, QDX representation, insurance audit representation, business license assistance and more.</p>
      <p>I have experience working with a wide variety of clients from the point where they first decide they want to start a business. They are often unsure about what to do first- I have a lot of experience to offer you.</p>
    </div>
    <p class="abs web" style="left:19px;top:326px;color:var(--white)">www.ridgelineacct.com</p>

    <div class="abs media-tech" role="img" aria-label="Photo of a hand touching a glowing financial chart interface"></div>
    <div class="abs firm-box">We are a full-service Tax Firm firm licensed in VA. We offer a broad range of services for business owners, executives, and independent professionals. We are affordable, experienced, and friendly.</div>

    <p class="abs contact" style="top:254px">Ridgeline Accounting &amp; Consulting, LLC<br>2870 Alder Hollow Rd, PO Box 14<br>Fenwick, VA 20400</p>
    <p class="abs contact" style="top:311px">(555)014-2276<br>Fax: (555)019-3381<br>hello@ridgelineacct.com</p>

    <h2 class="abs headline"><span class="h-small">WHAT A JOY IT<br>IS TO WATCH</span><span class="h-big">SUCCESS<br>IN ACTION!</span></h2>

    <div class="abs brand"><div class="dot"></div><span>RIDGELINE ACCOUNTING<br>&amp; CONSULTING, LLC</span></div>
  </section>

</main>
</body>
</html>
```